Company Profile for Consulting Comany

Need Company profile to be designed in a professional way.

for inspiring :-
https://www.vimolia.net/gallery/5307462/COMPANY-PROFILE
https://www.vimolia.net/gallery/20934617/Biotech-Product-Catalog-No1-(Laminar-Air-Flow)
https://www.vimolia.net/gallery/38720954/RKT-Tramvale-Company-Profile-2014-(RKT-Rebrand-part-2)

Target Market(s)

Corporate

Industry/Entity Type

It Company

Font styles to use
Sans Serif

Requirements
Must have
• Landscape A4 size
• Must go with the logo branding
• Must Have Visual Identity is the most important
• Must Have mpty spaces

```html
<!DOCTYPE html>
<html lang="en">
<head>
<meta charset="utf-8">
<title>Back Cover – Company Profile</title>
<link href="https://fonts.googleapis.com/css2?family=Raleway:wght@400;800&display=swap" rel="stylesheet">
<style>
  :root {
    --page-bg: #e6e7e9;
    --brand-teal: #1d97bd;
    --brand-teal-deep: #187e9e;
    --strip-grey: #3c3d3f;
    --sky-light: #d9d9d9;
    --sky-mid: #a9a9a9;
    --ground: #5b5b5b;
    --text-light: #ffffff;
  }
  * { box-sizing: border-box; margin: 0; padding: 0; }
  html, body {
    width: 1200px; height: 880px; overflow: hidden;
    background: var(--page-bg);
    font-family: "Raleway", sans-serif;
  }
  .back-cover {
    position: absolute; left: 50px; top: 51px;
    width: 1100px; height: 778px;
    background: var(--brand-teal);
    overflow: hidden;
  }
  .top-band {
    position: absolute; left: 0; top: 0; width: 100%; height: 110px;
    background: linear-gradient(90deg, var(--brand-teal-deep), var(--brand-teal));
  }
  .side-strip {
    position: absolute; left: 0; top: 110px; width: 96px; height: 330px;
    background: var(--strip-grey);
  }
  .landscape-photo {
    position: absolute; left: 96px; top: 132px; width: 1004px; height: 308px;
    background: linear-gradient(180deg, var(--sky-mid) 0%, var(--sky-light) 45%, #cfcfcf 62%, var(--ground) 68%, #6a6a6a 100%);
  }
  .office {
    position: absolute; top: 462px;
    color: var(--text-light);
    text-align: right;
    font-size: 15.5px; line-height: 1.32; font-weight: 400;
  }
  .office-city {
    font-weight: 800; letter-spacing: 0.02em; font-size: 15.5px;
  }
  .office--khobar { right: 560px; }
  .office--dubai { right: 40px; top: 535px; }
</style>
</head>
<body>
  <section class="back-cover">
    <div class="top-band"></div>
    <div class="side-strip"></div>
    <div class="landscape-photo" role="img" aria-label="Black and white photograph of a lone broad tree on an open grassy plain under a cloudy sky"></div>

    <address class="office office--khobar">
      <p class="office-city">KHOBAR</p>
      <p>PO BOX 48210, Khobar 31870, SAUDI ARABIA</p>
      <p>14th Floor, Corniche Point Tower, Palm Crescent St.</p>
      <p>T 00966 13 555 0142</p>
      <p>E hello@northwardpartners.com</p>
    </address>

    <address class="office office--dubai">
      <p class="office-city">DUBAI</p>
      <p>PO BOX 207615, Dubai, UAE</p>
      <p>19th Floor, Harbour Square- Tower 1, Lumen Avenue</p>
      <p>T 00971 4 555 0187 | F 00971 4 555 0193</p>
      <p>E hello@northwardpartners.com</p>
    </address>
  </section>
</body>
</html>
```